Graphic Design Project

I am looking for a designer to create three simple kitchen tea towel designs using the following text (insert images where appropriate):

'Everything I am, I owe to spaghetti' - Marta Velucci (prefer red)

'Coogee, Bronte, Clovelly, Tamarama, Bondi' (These are names of Sydney beaches. Bondi is the most famous.)

'Desperate Housewife'

Artwork parameters for tea towels: 43cm width X 75cm length. The target market is 25 - 40yr old women.

The text should take up most of the available space on the towel.

There is the opportunity for ongoing work for the right designer.

Thank you for your time.

Target Market(s)

Women aged 25 - 40 who live in Sydney.

Industry/Entity Type

Graphic Design

Requirements
Nice to have
• The feel of the following website:
http://www.plumforkglow.com/

```html
<!DOCTYPE html>
<html lang="en">
<head>
<meta charset="utf-8">
<title>Tea Towel Series</title>
<link rel="stylesheet" href="https://fonts.googleapis.com/css2?family=Playfair+Display:wght@700;900&family=Libre+Baskerville:wght@700&family=Great+Vibes&family=Lobster&family=Arimo:wght@700&display=swap">
<style>
  :root {
    --backdrop: #f3f3f1;
    --linen: #ffffff;
    --linen-edge: #e2e2de;
    --chilli: #e9542b;
    --sand: #f6ba22;
    --tomato: #e71f2b;
    --tomato-tint: #fbd9db;
  }
  * { margin: 0; padding: 0; box-sizing: border-box; }
  html, body { width: 1200px; height: 808px; overflow: hidden; }
  body { background: var(--backdrop); position: relative; }

  .towel {
    position: absolute;
    top: 190px;
    width: 370px;
    height: 590px;
    background: var(--linen);
    border: 1px solid var(--linen-edge);
    box-shadow: 0 2px 6px rgba(0,0,0,0.08);
  }
  .towel--housewife { left: 20px; }
  .towel--beaches { left: 415px; }
  .towel--spaghetti { left: 810px; }

  /* Desperate Housewife */
  .housewife-title {
    position: absolute;
    top: 52px;
    left: 0;
    width: 100%;
    text-align: center;
    font-family: "Playfair Display", serif;
    font-weight: 900;
    font-size: 104px;
    line-height: 96px;
    color: var(--chilli);
    letter-spacing: 2px;
  }
  .dot-rule {
    position: absolute;
    left: 102px;
    width: 166px;
    height: 6px;
  }
  .dot-rule--upper { top: 374px; }
  .dot-rule--lower { top: 520px; }
  .housewife-word {
    position: absolute;
    top: 410px;
    left: 0;
    width: 100%;
    text-align: center;
    font-family: "Great Vibes", cursive;
    font-size: 56px;
    color: var(--chilli);
  }

  /* Sydney beaches */
  .beach-list {
    position: absolute;
    top: 46px;
    left: 0;
    width: 100%;
    list-style: none;
    text-align: center;
    font-family: "Libre Baskerville", serif;
    font-weight: 700;
    color: var(--sand);
  }
  .beach-list li { line-height: 92px; }
  .beach--coogee { font-size: 70px; }
  .beach--bronte { font-size: 52px; }
  .beach--clovelly { font-size: 44px; }
  .beach--tamarama { font-size: 50px; }
  .beach--bondi { font-size: 62px; }

  /* Spaghetti quote */
  .quote-frame {
    position: absolute;
    inset: 12px;
    border: 2px dotted var(--tomato);
  }
  .dot-field {
    position: absolute;
    left: 26px;
    width: 318px;
    background: var(--tomato-tint);
  }
  .dot-field--top { top: 28px; height: 128px; }
  .dot-field--bottom { top: 410px; height: 150px; }
  .quote {
    position: absolute;
    top: 176px;
    left: 0;
    width: 100%;
    text-align: center;
    font-family: "Lobster", cursive;
    font-size: 50px;
    line-height: 58px;
    color: var(--tomato);
  }
  .quote-author {
    position: absolute;
    top: 366px;
    right: 60px;
    font-family: "Arimo", sans-serif;
    font-weight: 700;
    font-size: 15px;
    color: var(--tomato);
  }
</style>
</head>
<body>

  <section class="towel towel--housewife">
    <h1 class="housewife-title">DES<br>PER<br>ATE</h1>
    <svg class="dot-rule dot-rule--upper" viewBox="0 0 166 6" aria-hidden="true">
      <line x1="3" y1="3" x2="163" y2="3" stroke="var(--chilli)" stroke-width="5" stroke-linecap="round" stroke-dasharray="0 7"/>
    </svg>
    <p class="housewife-word">housewife</p>
    <svg class="dot-rule dot-rule--lower" viewBox="0 0 166 6" aria-hidden="true">
      <line x1="3" y1="3" x2="163" y2="3" stroke="var(--chilli)" stroke-width="5" stroke-linecap="round" stroke-dasharray="0 7"/>
    </svg>
  </section>

  <section class="towel towel--beaches">
    <ul class="beach-list">
      <li class="beach--coogee">Coogee</li>
      <li class="beach--bronte">BRONTE</li>
      <li class="beach--clovelly">CLOVELLY</li>
      <li class="beach--tamarama">Tamarama</li>
      <li class="beach--bondi">BONDI</li>
    </ul>
  </section>

  <section class="towel towel--spaghetti">
    <div class="quote-frame"></div>
    <div class="dot-field dot-field--top" role="img" aria-label="Red polka dot pattern"></div>
    <blockquote class="quote">“Everything<br>I am, I owe to<br>spaghetti”</blockquote>
    <p class="quote-author">- Marta Velucci</p>
    <div class="dot-field dot-field--bottom" role="img" aria-label="Red polka dot pattern"></div>
  </section>

</body>
</html>
```